New Tech Support Service needs a website design

We need a web design for a new product we are developing that provides tech support to consumers for a small ongoing monthly fee. We are looking for a fresh, technology look and feel. We want the site to have a tech feel - yet not intimidating. Simple and welcoming. We are in need of an initial landing page, sign on page, and a product home page.

Thank you to everyone who submitted designs. It was a very difficult decision!

Industry/Entity Type

Tech

```html
<!DOCTYPE html>
<html lang="en">
<head>
<meta charset="utf-8">
<title>A Bold Statement Through Web Design</title>
<link href="https://fonts.googleapis.com/css2?family=Bebas+Neue&family=Open+Sans:wght@300;400&display=swap" rel="stylesheet">
<style>
  :root {
    --hero-blue: #3a86c8;
    --hero-blue-deep: #2a6aa6;
    --hero-blue-light: #4d98d6;
    --band: rgba(18, 48, 78, 0.72);
    --white: #ffffff;
    --icon-grey: #8a8a8a;
  }
  * { margin: 0; padding: 0; box-sizing: border-box; }
  html, body { width: 1200px; height: 900px; overflow: hidden; }
  body { font-family: "Open Sans", Arial, sans-serif; color: var(--white); }
  .hero {
    position: relative; width: 1200px; height: 900px; overflow: hidden;
  }
  .hero-photo {
    position: absolute; inset: 0;
    background:
      radial-gradient(ellipse at 80% 55%, var(--hero-blue-light) 0%, transparent 55%),
      radial-gradient(ellipse at 15% 20%, var(--hero-blue-deep) 0%, transparent 50%),
      linear-gradient(180deg, var(--hero-blue) 0%, #3680c2 60%, var(--hero-blue-deep) 100%);
  }
  .site-header {
    position: absolute; top: 0; left: 0; right: 0; height: 90px;
  }
  .brand {
    position: absolute; left: 60px; top: 30px;
    font-weight: 300; font-size: 20px; letter-spacing: 2.4px; line-height: 30px;
  }
  .main-nav {
    position: absolute; right: 21px; top: 35px;
    display: flex; gap: 29px; list-style: none;
    font-size: 15px; line-height: 20px;
  }
  .settings-toggle {
    position: absolute; left: 0; top: 100px; width: 39px; height: 40px;
    background: var(--white); display: flex; align-items: center; justify-content: center;
  }
  .statement-band {
    position: absolute; left: 0; top: 383px; width: 1200px; height: 157px;
    background: var(--band); text-align: center;
  }
  .statement-title {
    font-family: "Bebas Neue", Impact, sans-serif; font-weight: 400;
    font-size: 60px; letter-spacing: 1.2px; line-height: 62px;
    margin-top: 22px;
  }
  .statement-text {
    font-weight: 300; font-size: 21px; line-height: 25px; margin-top: -1px;
  }
  .scroll-cue {
    position: absolute; left: 582px; top: 761px; width: 36px; height: 124px;
  }
</style>
</head>
<body>
<main class="hero">
  <div class="hero-photo" role="img" aria-label="Blue-tinted photo of a desk with a keyboard, pen holder and a hand writing on a notepad"></div>

  <header class="site-header">
    <div class="brand">Brightwire</div>
    <ul class="main-nav">
      <li>Home</li><li>Services</li><li>About</li><li>Portfolio</li>
      <li>Pricing</li><li>Our Team</li><li>Contact</li>
    </ul>
  </header>

  <div class="settings-toggle">
    <svg width="24" height="24" viewBox="0 0 24 24" aria-hidden="true">
      <g fill="var(--icon-grey)">
        <circle cx="12" cy="12" r="7.5"/>
        <rect x="10" y="1.5" width="4" height="5" rx="1"/>
        <rect x="10" y="17.5" width="4" height="5" rx="1"/>
        <rect x="1.5" y="10" width="5" height="4" rx="1"/>
        <rect x="17.5" y="10" width="5" height="4" rx="1"/>
        <rect x="10" y="1.5" width="4" height="5" rx="1" transform="rotate(45 12 12)"/>
        <rect x="10" y="17.5" width="4" height="5" rx="1" transform="rotate(45 12 12)"/>
        <rect x="1.5" y="10" width="5" height="4" rx="1" transform="rotate(45 12 12)"/>
        <rect x="17.5" y="10" width="5" height="4" rx="1" transform="rotate(45 12 12)"/>
      </g>
      <circle cx="12" cy="12" r="3.2" fill="#ffffff"/>
    </svg>
  </div>

  <section class="statement-band">
    <h1 class="statement-title">A Bold Statement Through Web Design</h1>
    <p class="statement-text">Web designs heavily influence the way visitors visualize your company<br>Lets capitalize on this opportunity!</p>
  </section>

  <svg class="scroll-cue" viewBox="0 0 36 124" aria-label="Scroll down">
    <circle cx="18" cy="18" r="17" fill="#ffffff"/>
    <polyline points="10,15 18,23 26,15" fill="none" stroke="var(--hero-blue-deep)" stroke-width="4" stroke-linecap="round" stroke-linejoin="round"/>
    <polyline points="13,51 18,56 23,51" fill="none" stroke="#ffffff" stroke-width="2.5" stroke-linecap="round" stroke-linejoin="round"/>
    <circle cx="18" cy="75" r="2.5" fill="#ffffff"/>
    <circle cx="18" cy="95" r="2.5" fill="#ffffff"/>
    <circle cx="18" cy="116" r="2.5" fill="#ffffff"/>
  </svg>
</main>
</body>
</html>
```